Webdesign für  Kranken- und Seniorenpflege
Webdesign für Kranken- und Seniorenpflege
Zielgruppe
Ambulante Kranken- und Seniorenpflege
Tagespflege in Limbach-Oberfrohna, Mittweida und Chemnitz
Palliativpflege
Aufgabenstellung
- Erstellung in Adobe Photoshop
- Orientieren Sie sich am Socialmedia-Auftritt des Kunden

```html
<!DOCTYPE html>
<html lang="de">
<head>
<meta charset="utf-8">
<title>Lindwerk Pflege – Ambulante Pflege Sachsen</title>
<link rel="stylesheet" href="https://fonts.googleapis.com/css2?family=Fira+Sans:wght@500;600&family=Open+Sans:wght@400;600;700&family=Roboto+Condensed:wght@400;500&display=swap">
<style>
:root{
  --crimson:#9b0a40;
  --sun:#f7a600;
  --ink:#333;
  --ink-soft:#444;
  --white:#fff;
}
*{box-sizing:border-box;margin:0;padding:0}
html,body{width:1200px;height:3042px;overflow:hidden;background:var(--white)}
body{position:relative;font-family:"Open Sans",Arial,sans-serif;color:var(--ink)}
.abs{position:absolute}

/* header */
.brand-name{font-family:"Fira Sans",Arial,sans-serif;font-weight:600;font-size:32px;color:var(--crimson);white-space:nowrap}
.header-brand{left:57px;top:40px}
.hotline{left:959px;top:0;width:184px;height:72px;background:var(--crimson);border-radius:0 0 8px 8px;color:var(--white);padding:13px 16px}
.hotline small{display:block;font-family:"Roboto Condensed",Arial,sans-serif;font-size:12px}
.hotline strong{display:block;font-family:"Roboto Condensed",Arial,sans-serif;font-weight:500;font-size:25px;letter-spacing:.5px;line-height:1.1}
.main-nav{left:60px;right:58px;top:126px;display:flex;justify-content:space-between;font-family:"Roboto Condensed",Arial,sans-serif;font-size:17px;color:#111}
.main-nav .active{color:var(--crimson)}
.nav-rule{left:0;top:164px;width:1200px;height:1px;background:#ddd}

/* hero */
.hero-panel{left:0;top:165px;width:489px;height:476px;background:var(--crimson)}
.hero-title{left:60px;top:303px;font-family:"Fira Sans",Arial,sans-serif;font-weight:600;font-size:46px;line-height:49px;color:var(--sun)}
.hero-sub{left:60px;top:411px;width:345px;font-size:17.5px;line-height:27px;color:var(--white)}
.hero-photo{left:489px;top:165px;width:711px;height:476px;background:linear-gradient(120deg,#c9a98d,#8b5a4a 45%,#d8c3b5)}

.social-tab{left:1109px;width:91px;height:94px;background:var(--sun);border-radius:12px 0 0 12px;display:flex;align-items:center;justify-content:center}

/* service cards */
.card{width:534px}
.card-photo{height:259px;border-radius:10px}
.card-title{margin:22px 1px 0;font-family:"Fira Sans",Arial,sans-serif;font-weight:600;font-size:37px;line-height:38px;color:var(--crimson)}
.card-text{margin:16px 1px 0;width:390px;font-size:17.5px;line-height:24.5px;color:var(--ink-soft)}
.btn{display:inline-block;background:var(--crimson);color:var(--white);font-weight:700;font-size:14.5px;letter-spacing:.6px;padding:11px 18px;border-radius:2px}
.card .btn{margin:26px 1px 0}

/* jobs */
.jobs{left:57px;top:1935px;width:1086px;height:472px;background:var(--crimson);border-radius:10px;overflow:hidden}
.jobs-photo{position:absolute;left:0;top:0;width:691px;height:472px;background:linear-gradient(180deg,#a9b6a3,#8a3249 55%,#6f1a30)}
.jobs-body{position:absolute;left:727px;top:115px;width:330px;color:var(--white)}
.jobs-title{font-family:"Fira Sans",Arial,sans-serif;font-weight:600;font-size:36px;line-height:38px;color:var(--sun)}
.jobs-text{margin-top:18px;font-size:17.5px;line-height:24.5px;width:322px}
.btn-light{margin-top:26px;background:var(--white);color:var(--crimson)}

/* news */
.news-heading{left:0;width:1200px;top:2470px;text-align:center;font-family:"Fira Sans",Arial,sans-serif;font-weight:600;font-size:48px;color:var(--crimson)}
.news-item{top:2560px;width:325px}
.news-title{font-family:"Fira Sans",Arial,sans-serif;font-weight:500;font-size:25px;line-height:28px;color:#3a3a3a}
.news-text{margin-top:14px;font-size:14px;line-height:20px;color:var(--ink-soft)}
.more{display:inline-block;margin-top:10px;font-weight:700;font-size:13.5px;letter-spacing:1.4px;color:var(--crimson);text-decoration:underline}
.news-overview{left:499px;top:2807px}

/* footer */
.footer-links{left:57px;top:2978px;display:flex;gap:31px;font-size:12px;color:var(--crimson)}
.footer-links a{color:var(--crimson);text-decoration:underline;letter-spacing:.5px}
.footer-brand{left:900px;top:2960px}
</style>
</head>
<body>

<header>
  <div class="abs brand-name header-brand">Lindwerk Pflege</div>
  <div class="abs hotline"><small>Unsere kostenlose Telefon-Nr:</small><strong>0800-5550123</strong></div>
  <nav class="abs main-nav">
    <span class="active">Startseite</span><span>Kranken- und Seniorenpflege</span><span>Tagespflege</span><span>Palliativpflege</span><span>Pflegeberatung</span><span>Standorte</span><span>Stellenangebote</span><span>Aktuelles</span>
  </nav>
  <div class="abs nav-rule"></div>
</header>

<section>
  <div class="abs hero-panel"></div>
  <h1 class="abs hero-title">Lindwerk Pflege<br>Sachsen</h1>
  <p class="abs hero-sub">Ambulanter Pflegedienst im Raum Mittweida, Chemnitz, Limbach-Oberfrohna und Umgebung (Sachsen)</p>
  <div class="abs hero-photo" role="img" aria-label="Foto: Pflegerin lacht gemeinsam mit einer älteren Dame mit Strickmütze"></div>
</section>

<div class="abs social-tab" style="top:573px" aria-label="Soziales Netzwerk"><svg width="46" height="46" viewBox="0 0 46 46"><circle cx="23" cy="23" r="19" fill="none" stroke="#fff" stroke-width="4"/></svg></div>
<div class="abs social-tab" style="top:685px" aria-label="Soziales Netzwerk"><svg width="46" height="46" viewBox="0 0 46 46"><rect x="5" y="5" width="36" height="36" rx="4" fill="none" stroke="#fff" stroke-width="4"/></svg></div>

<article class="abs card" style="left:57px;top:712px">
  <div class="card-photo" role="img" aria-label="Foto: ältere Frau im Beratungsgespräch" style="background:linear-gradient(110deg,#e4e6e3,#7f9fc8 45%,#d9dcdc)"></div>
  <h2 class="card-title">Beratung im Pflegefall -<br>wir helfen Ihnen weiter.</h2>
  <p class="card-text">Unsere Pflegeberater vor Ort unterstützen Sie, eine passgenaue Lösung für Ihre Situation zu finden und unterstützen Sie bei den Anträgen.</p>
  <span class="btn">MEHR ERFAHREN</span>
</article>
<article class="abs card" style="left:613px;top:712px">
  <div class="card-photo" role="img" aria-label="Foto: Seniorin und junge Pflegerin lächeln gemeinsam" style="background:linear-gradient(100deg,#cfc6bd,#b89a88 50%,#8a2a3e)"></div>
  <h2 class="card-title">Kranken- &amp;<br>Seniorenpflege</h2>
  <p class="card-text">Als inhabergeführtes Unternehmen liegen uns die persönlichen, individuelle Betreuung und Versorgung von Pflegebedürftigen besonders am Herzen.</p>
  <span class="btn">MEHR ERFAHREN</span>
</article>
<article class="abs card" style="left:57px;top:1319px">
  <div class="card-photo" role="img" aria-label="Foto: Hände beim Brettspiel in der Tagespflege" style="background:linear-gradient(110deg,#f0eeea,#d6b47c 50%,#ecebe7)"></div>
  <h2 class="card-title">Tagespflege - Wohlfühlen<br>für alle</h2>
  <p class="card-text" style="width:500px">In der Tagespflege bieten wir, neben der Integration in unsere Sozialgemeinschaft, eine Rundum-Betreuung für Senioren mit interessanten und abwechslungsreichen Tagesaktivitäten.</p>
  <span class="btn">MEHR ERFAHREN</span>
</article>
<article class="abs card" style="left:613px;top:1319px">
  <div class="card-photo" role="img" aria-label="Schwarzweißfoto: junge Hände halten alte Hände" style="background:linear-gradient(110deg,#8a8a8a,#c9c9c9 50%,#9a9a9a)"></div>
  <h2 class="card-title">Die letzten Tage und<br>Stunden</h2>
  <p class="card-text" style="width:425px">Die Zeit des Sterbens eines nahestehenden Menschen ist für viele Angehörige und Freunde eine Zeit der Krise, Angst und der Unsicherheit. Wir begleiten und helfen.</p>
  <span class="btn">MEHR ERFAHREN</span>
</article>

<section class="abs jobs">
  <div class="jobs-photo" role="img" aria-label="Gruppenfoto: Pflegeteam in roten Poloshirts vor einer Gaststätte"></div>
  <div class="jobs-body">
    <h2 class="jobs-title">Stellenangebote -<br>Zeit für Helden!</h2>
    <p class="jobs-text">Unser Team ist aufgeschlossen und mit Freude bei der Arbeit! Bereichern Sie unser Unternehmen mit Ihrer Fachkompetenz und Leidenschaft!</p>
    <span class="btn btn-light">ZU DEN STELLEN</span>
  </div>
</section>

<h2 class="abs news-heading">Aktuelles:</h2>
<article class="abs news-item" style="left:57px">
  <h3 class="news-title">Sommerfest in der Tagespflege „Lindenhof“</h3>
  <p class="news-text">Sommereinklang in der Tagespflege „Lindenhof“ in Chemnitz. Bei sommerlichen Temperaturen und strahlenden Sonnenschein verweilten die Tagesgäste auf unserer großzügigen Terrasse. Unsere Betreuungskraft Katrin sorgte für ...</p>
  <span class="more">WEITERLESEN</span>
</article>
<article class="abs news-item" style="left:428px">
  <h3 class="news-title">Wochenausklang am Schwanenteich in Mittweida</h3>
  <p class="news-text">Die vergangene Woche haben wir mit unseren Gästen aus der Tagespflege „Am Markt“ am Schwanenteich in Mittweida ausklingen lassen. Nach einem Spaziergang durch den Park und einer Tasse Kaffee ...</p>
  <span class="more">WEITERLESEN</span>
</article>
<article class="abs news-item" style="left:797px">
  <h3 class="news-title">Maifest in der Tagespflege „Am Markt“</h3>
  <p class="news-text">Zu unserem Maifest in der Tagespflege „Am Markt“ in Mittweida erlebten unsere Gäste bei schönstem Wetter einen abwechslungs-reichen Tag. Mit leckerer Maibowle, Nudel-salat und Bratwurst vom Grill, gab ...</p>
  <span class="more">WEITERLESEN</span>
</article>
<span class="abs btn news-overview">ÜBERSICHT AKTUELLES</span>

<footer>
  <div class="abs footer-links"><span>© 2022 Lindwerk Pflege</span><a>IMPRESSUM</a><a>DATENSCHUTZ</a><a>KONTAKT</a></div>
  <div class="abs brand-name footer-brand">Lindwerk Pflege</div>
</footer>

</body>
</html>
```